Increased budget: GUI redesign: 10 year old user interface needs modern look-and-feel

UPDATE: Please DO look at more than only th eone image I attached! Almost all designs are simply reworks of that one picture. That is not what we are looking for. Check out the video to understand what the product does, and try to make something better.
We have an existing app (see https://www.vornatek.com/downloadTunePilot.php?vers=3_9_1_140964&dir=Vornatek_OEM/3_9_1_140964&name=DSP_Control_Software) which needs refreshing. See also a video here: https://vornatek-oem.com/software/ and the user manual attached here. The GUI is now 800x400 pixels, which is too small; and not scalable, which will be fixed in the future. We need a new, modern look-and-feel, and images that can be exported from the design in various sizes. The current design is attached as well as a collection of PNG files. The overall layout can stay similar, although we are open to good ideas for improvements. The design should be targeted at professional users, not end users; the product is used by audio professionals (e.g. sound engineers, loudspeaker designers). Also see our web version: https://www.vornatek.com/tunepilot/skins/1_1_2/container.html?MAC=Demo%201x2
The winner will also be asked to do a full design of the application GUI (based on the design done here), with several more windows etc, and additional payment depending on the work to be done.

Target Market(s)

Professional audio

Industry/Entity Type

Audio / Industrial

Font styles to use
Other font styles liked:
• Futura (not mandatory)

Colors

Designer to choose colors to be used in the design.

Requirements
Must have
• Modern, timeless design, not too bling bling
Nice to have
• Flat design
Should not have
• 3D, bling bling, many colours, etc

```html
<!DOCTYPE html>
<html lang="en">
<head>
<meta charset="utf-8">
<title>TunePilot DSP Command Centre</title>
<link href="https://fonts.googleapis.com/css2?family=Roboto:wght@400;500;700&display=swap" rel="stylesheet">
<style>
:root{
  --bg-top:#2a2a2e;
  --bg-bottom:#1c1c1f;
  --panel:#29292d;
  --button:#39383d;
  --button-border:#45444a;
  --text:#ffffff;
  --text-dark:#1b1b1d;
  --muted:#cfcfd4;
  --track:#38383c;
  --tick:#8a8a90;
  --tab:#0e0e10;
  --tab-border:#4a4a50;
  --ok:#4be01b;
  --alert:#ff1616;
}
*{box-sizing:border-box;margin:0;padding:0}
html,body{width:1200px;height:840px;overflow:hidden}
body{
  position:relative;
  background:linear-gradient(160deg,var(--bg-top),var(--bg-bottom));
  font-family:"Roboto",Arial,sans-serif;color:var(--text);
}
.abs{position:absolute}
.side-panel{left:25px;top:35px;width:256px;height:699px;background:var(--panel);border-radius:8px;box-shadow:0 6px 20px rgba(0,0,0,.35)}
.label{position:absolute;left:56px;font-size:17px;font-weight:500;line-height:1}
.btn{position:absolute;height:40px;background:var(--button);border:2px solid var(--button-border);border-radius:4px;
  display:flex;align-items:center;justify-content:center;font-size:12px;font-weight:700;letter-spacing:.2px}
.btn.half{width:88px}
.btn.full{left:57px;width:187px}
.btn.white{background:#fff;color:var(--text-dark);border-color:#fff}
.btn.input{background:#fff;color:var(--text-dark);border:3px solid var(--button)}
.btn .caret{position:absolute;right:22px;top:13px;width:0;height:0;border-left:7px solid #fff;border-top:5px solid transparent;border-bottom:5px solid transparent}
.lamp{position:absolute;left:224px;width:24px;height:24px;border-radius:50%;border:3px solid #fff}
.lamp.ok{background:var(--ok)}
.lamp.alert{background:var(--alert)}
.toggle{left:143px;top:682px;width:16px;height:36px;border-radius:8px;border:2px solid #55545a;background:#1e1e21}
.toggle::after{content:"";position:absolute;left:0px;bottom:1px;width:12px;height:12px;border-radius:50%;background:var(--ok)}
.title{left:308px;top:74px;font-size:29px;font-weight:700;letter-spacing:.3px}
.icon-btn{top:75px;width:30px;height:30px;border-radius:50%;background:#3a393e;display:flex;align-items:center;justify-content:center}
.mixer-panel{left:305px;top:127px;width:870px;height:607px;background:var(--panel);border-radius:8px}
.mixer{left:0;top:0}
.tab{position:absolute;top:758px;width:46px;height:46px;background:var(--tab);border:2px solid var(--tab-border);
  display:flex;align-items:center;justify-content:center;font-size:10px;font-weight:700}
</style>
</head>
<body>

<aside class="abs side-panel"></aside>
<div class="label" style="top:85px">Local presets</div>
<div class="btn half" style="left:57px;top:118px">STORE</div>
<div class="btn half" style="left:156px;top:118px">LOAD</div>

<div class="label" style="top:184px">Local presets</div>
<div class="btn full white" style="top:216px">NO NAME</div>
<div class="btn full" style="top:269px">1 : EMPTY PRESET<span class="caret"></span></div>
<div class="btn half" style="left:57px;top:322px">STORE</div>
<div class="btn half" style="left:156px;top:322px">LOAD</div>

<div class="label" style="top:396px">Link</div>
<div class="lamp ok" style="top:393px"></div>
<div class="btn full" style="top:428px">VX428<span class="caret"></span></div>

<div class="label" style="top:494px">Unit name</div>
<div class="btn full input" style="top:527px">VX428</div>

<div class="label" style="top:593px">Status</div>
<div class="lamp alert" style="top:590px"></div>
<div class="btn full" style="top:626px">DETAILS</div>
<div class="abs toggle"></div>

<h1 class="abs title">TUNEPILOT DSP COMMAND CENTRE</h1>
<div class="abs icon-btn" style="left:1099px" aria-label="Settings">
  <svg width="14" height="14" viewBox="0 0 24 24"><g fill="#fff"><circle cx="12" cy="12" r="7"/><rect x="10" y="1" width="4" height="22" rx="1"/><rect x="1" y="10" width="22" height="4" rx="1"/><rect x="10" y="1" width="4" height="22" rx="1" transform="rotate(45 12 12)"/><rect x="10" y="1" width="4" height="22" rx="1" transform="rotate(-45 12 12)"/></g><circle cx="12" cy="12" r="3" fill="#3a393e"/></svg>
</div>
<div class="abs icon-btn" style="left:1141px" aria-label="Close">
  <svg width="12" height="12" viewBox="0 0 12 12"><path d="M2 2L10 10M10 2L2 10" stroke="#fff" stroke-width="2.6" stroke-linecap="round"/></svg>
</div>

<section class="abs mixer-panel"></section>

<svg class="abs mixer" width="1200" height="840" viewBox="0 0 1200 840" font-family="Roboto, Arial, sans-serif">
  <defs>
    <pattern id="scaleTicks" patternUnits="userSpaceOnUse" x="-36" y="167" width="24" height="41">
      <line x1="0" y1="0.5" x2="24" y2="0.5" stroke="#a0a0a6" stroke-width="1"/>
      <line x1="17" y1="3.9" x2="24" y2="3.9" stroke="var(--tick)" stroke-width=".8"/>
      <line x1="17" y1="7.3" x2="24" y2="7.3" stroke="var(--tick)" stroke-width=".8"/>
      <line x1="17" y1="10.7" x2="24" y2="10.7" stroke="var(--tick)" stroke-width=".8"/>
      <line x1="17" y1="14.2" x2="24" y2="14.2" stroke="var(--tick)" stroke-width=".8"/>
      <line x1="17" y1="17.6" x2="24" y2="17.6" stroke="var(--tick)" stroke-width=".8"/>
      <line x1="10" y1="21" x2="24" y2="21" stroke="var(--tick)" stroke-width=".8"/>
      <line x1="17" y1="24.4" x2="24" y2="24.4" stroke="var(--tick)" stroke-width=".8"/>
      <line x1="17" y1="27.8" x2="24" y2="27.8" stroke="var(--tick)" stroke-width=".8"/>
      <line x1="17" y1="31.2" x2="24" y2="31.2" stroke="var(--tick)" stroke-width=".8"/>
      <line x1="17" y1="34.6" x2="24" y2="34.6" stroke="var(--tick)" stroke-width=".8"/>
      <line x1="17" y1="38" x2="24" y2="38" stroke="var(--tick)" stroke-width=".8"/>
    </pattern>
    <g id="fader">
      <rect x="-36" y="166.5" width="24" height="411" fill="url(#scaleTicks)"/>
      <line x1="0" y1="167" x2="0" y2="576" stroke="var(--track)" stroke-width="5" stroke-linecap="round"/>
      <circle cx="0" cy="248" r="8" fill="#fff" stroke="#6a6a70" stroke-width="1.5"/>
    </g>
    <rect id="sq" x="-5.5" y="-5.5" width="11" height="11" rx="1.5" fill="#6e6e74" stroke="#8a8a90"/>
    <g id="val"><rect x="-15" y="-15" width="30" height="30" rx="6" fill="#fff"/><text y="4" text-anchor="middle" font-size="10" font-weight="700" fill="#1b1b1d">0</text></g>
  </defs>

  <g class="db-left" font-size="9.5" fill="#fff" text-anchor="end">
    <text x="355" y="170">+12</text><text x="355" y="211">+6</text><text x="355" y="252">0+</text>
    <text x="355" y="293">-6</text><text x="355" y="334">-12</text><text x="355" y="375">-18</text>
    <text x="355" y="416">-24</text><text x="355" y="457">-30</text><text x="355" y="498">-36</text>
    <text x="355" y="539">-42</text><text x="355" y="580">-48</text>
  </g>
  <g class="db-right" font-size="9.5" fill="#fff">
    <text x="1128" y="170">+12</text><text x="1131" y="211">+6</text><text x="1131" y="252">0+</text>
    <text x="1133" y="293">-6</text><text x="1131" y="334">-12</text><text x="1131" y="375">-18</text>
    <text x="1131" y="416">-24</text><text x="1131" y="457">-30</text><text x="1131" y="498">-36</text>
    <text x="1131" y="539">-42</text><text x="1131" y="580">-48</text>
  </g>

  <g class="faders">
    <use href="#fader" x="399"/><use href="#fader" x="456"/><use href="#fader" x="512"/><use href="#fader" x="569"/>
    <use href="#fader" x="702"/><use href="#fader" x="758"/><use href="#fader" x="815"/><use href="#fader" x="871"/>
    <use href="#fader" x="921"/><use href="#fader" x="977"/><use href="#fader" x="1034"/><use href="#fader" x="1090"/>
    <rect x="1085" y="166.5" width="24" height="411" fill="url(#scaleTicks)" transform="translate(1206 0) scale(-1 1) translate(-36 0)" opacity="0"/>
  </g>
  <rect x="1112" y="166.5" width="24" height="411" fill="url(#scaleTicks)" transform="translate(2236 0) scale(-1 1)"/>

  <text x="326" y="638" font-size="14" font-weight="700" fill="#fff">Link</text>
  <line x1="366" y1="633" x2="1127" y2="633" stroke="#56565c" stroke-width="1"/>
  <g class="link-upper">
    <use href="#sq" x="415" y="634"/><use href="#sq" x="528" y="634"/><use href="#sq" x="724" y="634"/>
    <use href="#sq" x="780" y="634"/><use href="#sq" x="837" y="634"/><use href="#sq" x="942" y="634"/><use href="#sq" x="1055" y="634"/>
  </g>
  <g class="gain-values">
    <use href="#val" x="388" y="662"/><use href="#val" x="444" y="662"/><use href="#val" x="500" y="662"/><use href="#val" x="556" y="662"/>
    <use href="#val" x="696" y="662"/><use href="#val" x="752" y="662"/><use href="#val" x="809" y="662"/><use href="#val" x="864" y="662"/>
    <use href="#val" x="914" y="662"/><use href="#val" x="970" y="662"/><use href="#val" x="1026" y="662"/><use href="#val" x="1082" y="662"/>
  </g>
  <line x1="366" y1="698" x2="1127" y2="698" stroke="#56565c" stroke-width="1"/>
  <g class="link-lower">
    <use href="#sq" x="389" y="698"/><use href="#sq" x="444" y="698"/><use href="#sq" x="501" y="698"/><use href="#sq" x="557" y="698"/>
    <use href="#sq" x="697" y="698"/><use href="#sq" x="753" y="698"/><use href="#sq" x="809" y="698"/><use href="#sq" x="866" y="698"/>
    <use href="#sq" x="916" y="698"/><use href="#sq" x="972" y="698"/><use href="#sq" x="1028" y="698"/><use href="#sq" x="1084" y="698"/>
  </g>
</svg>

<nav class="tabs">
  <div class="tab" style="left:92px">Main</div>
  <div class="tab" style="left:148px">X-over</div>
  <div class="tab" style="left:363px">In 1</div>
  <div class="tab" style="left:419px">In 2</div>
  <div class="tab" style="left:475px">In 3</div>
  <div class="tab" style="left:531px">In 4</div>
  <div class="tab" style="left:666px">Out 1</div>
  <div class="tab" style="left:722px">Out 2</div>
  <div class="tab" style="left:778px">Out 3</div>
  <div class="tab" style="left:835px">Out 4</div>
  <div class="tab" style="left:890px">Out 5</div>
  <div class="tab" style="left:947px">Out 6</div>
  <div class="tab" style="left:1003px">Out 7</div>
  <div class="tab" style="left:1059px">Out 8</div>
</nav>

</body>
</html>
```